Brookhollow dog Kennel -Loyalty Card

We are a bod boarding and training Kennel located in Egypt and we would like to design a member loyalty card. The card need to be fun, funky. I would like the logo to appear on the card. On the back side we will list the benefits and on the bottom side of the card will will have the logos of our partner companies

Target Market(s)

clientele from dog lovers. Age 25 and above. 65% women.

Industry/Entity Type

Training

Font styles to use
Sans Serif

Colors
0555a3
33a6d7
0792cd

Requirements
Must have
• Brookhollow Logo and bleu colours.
Nice to have
• a dog figure
Should not have
• dark serious colours or aggressive looking dogs or dog breeds

```html
<!DOCTYPE html>
<html lang="en">
<head>
<meta charset="utf-8">
<title>Brookhollow Training – Loyalty Card</title>
<link href="https://fonts.googleapis.com/css2?family=Oswald:wght@400;500;700&display=swap" rel="stylesheet">
<style>
  :root {
    --stage: #ece7e1;
    --orange: #f39a1e;
    --orange-deep: #e8800f;
    --sun: #ffe02a;
    --blue: #0555a3;
    --blue-mid: #0792cd;
    --blue-light: #33a6d7;
    --yellow: #ffe81c;
    --white: #ffffff;
    --ink: #111111;
    --rim: #f6c98a;
  }
  * { margin: 0; padding: 0; box-sizing: border-box; }
  html, body { width: 1200px; height: 1200px; overflow: hidden; }
  body {
    background: var(--stage);
    font-family: "Oswald", "Arial Narrow", sans-serif;
    position: relative;
  }
  .card {
    position: absolute;
    top: 78px;
    width: 510px;
    height: 807px;
    border-radius: 24px;
    overflow: hidden;
    background: radial-gradient(circle at 50% 52%, var(--sun) 0%, #ffc21f 22%, var(--orange) 52%, var(--orange-deep) 100%);
  }
  .card--front { left: 75px; }
  .card--back { left: 623px; background: radial-gradient(circle at 50% 48%, var(--sun) 0%, #ffc21f 18%, var(--orange) 45%, var(--orange-deep) 100%); }
  .panel {
    position: absolute;
    background: var(--blue);
    border: 2px solid var(--rim);
    color: var(--white);
    text-align: center;
  }
  .dotted { position: absolute; left: 24px; right: 24px; border-top: 2px dotted var(--white); }
  .ornament { position: absolute; border-radius: 40px 40px 6px 6px; }

  /* front */
  .front-header { left: 29px; top: 25px; width: 450px; height: 190px; }
  .front-header .ornament { left: 55px; top: 10px; width: 340px; height: 54px; background: linear-gradient(180deg, var(--yellow), #e9c914); opacity: .85; }
  .loyalty-title { position: absolute; left: 0; right: 0; top: 66px; font-size: 46px; font-weight: 700; color: var(--yellow); line-height: 1; letter-spacing: .5px; }
  .loyalty-sub { position: absolute; left: 0; right: 0; top: 141px; font-size: 26px; font-weight: 500; line-height: 1; }
  .front-header .dotted.top { top: 132px; }
  .front-header .dotted.bottom { top: 176px; }

  .dog-figure {
    position: absolute; left: 250px; top: 200px; width: 190px; height: 310px;
    border-radius: 90px 90px 40px 40px;
    background: radial-gradient(circle at 50% 40%, #ffffff 0%, #f3ece4 45%, #c98a5a 100%);
    opacity: .92;
  }
  .mark { position: absolute; display: flex; align-items: center; gap: 8px; color: var(--blue); font-weight: 700; line-height: 1.05; }
  .mark__square { width: 22px; height: 22px; background: var(--blue); flex: none; }
  .front-mark { left: 70px; top: 430px; width: 170px; font-size: 26px; }

  .wordmark { position: absolute; left: 0; right: 0; text-align: center; font-size: 44px; font-weight: 700; color: var(--ink); line-height: 1; letter-spacing: .5px; white-space: nowrap; }
  .card--front .wordmark { top: 540px; }
  .card--back .wordmark { top: 530px; }

  .front-offer { left: 75px; top: 625px; width: 360px; height: 152px; text-align: left; }
  .tab { position: absolute; left: 50%; top: -12px; width: 30px; height: 14px; margin-left: -15px; background: var(--blue); border-radius: 15px 15px 0 0; }
  .avail-badge {
    position: absolute; left: 10px; top: 14px; width: 122px; height: 122px; border-radius: 50%;
    background: var(--yellow); border: 4px solid var(--white); box-shadow: 0 0 0 2px var(--ink);
    display: flex; align-items: center; justify-content: center; text-align: center;
    color: var(--ink); font-size: 22px; font-weight: 500; line-height: 1.1;
  }
  .offer-list { position: absolute; left: 152px; top: 22px; }
  .offer-list h3 { font-size: 26px; font-weight: 700; line-height: 1; margin-bottom: 8px; }
  .offer-list li { list-style: none; font-size: 18px; font-weight: 400; line-height: 26px; white-space: nowrap; }

  /* back */
  .back-ornament { left: 60px; top: 42px; width: 390px; height: 110px; background: linear-gradient(180deg, var(--blue-mid), var(--blue)); opacity: .75; }
  .details-panel { left: 77px; top: 107px; width: 358px; height: 395px; }
  .details-title { position: absolute; left: 0; right: 0; top: 30px; font-size: 40px; font-weight: 700; color: var(--yellow); line-height: 1; }
  .details-panel .dotted.top { top: 20px; }
  .details-panel .dotted.bottom { top: 80px; }
  .benefit { position: absolute; left: 16px; right: 16px; height: 50px; display: flex; align-items: center; text-align: left; }
  .benefit__rate { width: 72px; flex: none; font-size: 28px; font-weight: 500; line-height: 1; }
  .benefit__text { border-left: 2px solid var(--white); padding-left: 16px; font-size: 20px; line-height: 20px; font-weight: 400; white-space: nowrap; }
  .benefit--first { top: 113px; }
  .benefit--second { top: 178px; }
  .benefit--third { top: 243px; }
  .deserve { position: absolute; left: 0; right: 0; top: 325px; font-size: 40px; font-weight: 700; line-height: 1; }
  .partner-row { position: absolute; left: 0; right: 0; top: 700px; display: flex; justify-content: center; gap: 28px; }
  .partner-row .mark { position: static; font-size: 20px; }
</style>
</head>
<body>

<section class="card card--front" aria-label="Loyalty card front">
  <div class="panel front-header">
    <div class="ornament" role="img" aria-label="Yellow decorative flourish"></div>
    <h1 class="loyalty-title">YOUR LOYALTY PAYS</h1>
    <div class="dotted top"></div>
    <p class="loyalty-sub">IT’S SOMETHING WE LOVE TO DO!</p>
    <div class="dotted bottom"></div>
  </div>

  <div class="dog-figure" role="img" aria-label="Cartoon of a cheerful white and brown puppy sitting with a red collar"></div>

  <div class="mark front-mark"><span class="mark__square"></span><span>Brookhollow<br>Training</span></div>

  <div class="wordmark">BROOKHOLLOW TRAINING</div>

  <div class="panel front-offer">
    <span class="tab"></span>
    <div class="avail-badge">START<br>AVAILING<br>NOW!</div>
    <div class="offer-list">
      <h3>DISCOUNT ON:</h3>
      <ul>
        <li>All 1 PawPantry purchased</li>
        <li>Wash&amp; Walk services</li>
        <li>Brookhollow training courses</li>
      </ul>
    </div>
  </div>
</section>

<section class="card card--back" aria-label="Loyalty card back">
  <div class="ornament back-ornament" role="img" aria-label="Blue decorative flourish"></div>
  <div class="panel details-panel">
    <div class="dotted top"></div>
    <h2 class="details-title">DISCOUNT DETAILS</h2>
    <div class="dotted bottom"></div>
    <div class="benefit benefit--first"><span class="benefit__rate">5%</span><span class="benefit__text">Discount on all 1 PawPantry<br>purchased</span></div>
    <div class="benefit benefit--second"><span class="benefit__rate">10%</span><span class="benefit__text">discount on Wash&amp; Walk<br>services</span></div>
    <div class="benefit benefit--third"><span class="benefit__rate">10%</span><span class="benefit__text">Discount on Brookhollow train-<br>ing courses</span></div>
    <p class="deserve">YOU DESERVE IT!</p>
  </div>

  <div class="wordmark">BROOKHOLLOW TRAINING</div>

  <div class="partner-row">
    <div class="mark"><span class="mark__square"></span>Brookhollow Training</div>
    <div class="mark"><span class="mark__square"></span>Brookhollow Kennels</div>
  </div>
</section>

</body>
</html>
```